Vexaroo needs app design - Social app for a party on a budget

We need a design for our app called "Vexaroo", Vexaroo is an essential application that showcases the finest clubs in the city. The primary objective of the app is to provide users with insights into club ratings and beer prices, enabling them to locate the most cost-effective beer near their current location. You as a user will also have ability to rate different Additionally, users can view posts and images from various patrons, offering glimpses into the ambiance of the establishments to determine if they meet their preferences and requirements.

We imagine Vexaroo having a "gamification app desigin" as partying is like a game, you experience new adventures and take on new quests.
Allthough we are open for different designs, surprise us.

Keyfeatures:
1 - Splash/Login Page:
Allow users to log in or sign up using Google, Instagram, or Facebook credentials.
2 - Home Page/Announcements:
Display user-generated posts from different clubs and pubs, showcasing crowd levels and overall enjoyment.
Enable users to like posts, with sorting based on likes and proximity.
Access announcements from establishments about upcoming events, entrance fees, and performances.
3 - Search Page:
Provide a map displaying nearby pubs and clubs, with basic information such as rating, beer prices, and operating hours.
4 - List Page:
Present a comprehensive list of nearby clubs and pubs, sorted initially by rating.
Allow users to sort by beer prices, location, and other criteria.
Enable users to rate establishments using a 1-5 star system, with monthly winners prominently featured on the announcement page.
5 - My page:
Allow users to revisit and upload memories, including pictures, locations, dates, and times.
Provide an option to repost pictures on Instagram.
Feature a "Refer a Friend" button for users to earn complimentary memberships by referring friends who complete the registration process.

As mentioned these are only key features we imagine this app should have, feel free to play around with the design.

Requirements
Must have
• Key features meantioned in project description

```html
<!DOCTYPE html>
<html lang="en">
<head>
<meta charset="utf-8">
<title>Vexaroo – App Screens</title>
<link rel="stylesheet" href="https://fonts.googleapis.com/css2?family=Poppins:ital,wght@0,400;0,500;0,600;0,700;1,400&display=swap">
<style>
  :root{
    --stage:#2b2b2b;
    --ink:#262626;
    --ink-soft:#3a3a3a;
    --white:#ffffff;
    --cream:#fbf1d6;
    --foam:#f8e7b0;
    --beer:#f9dc2c;
    --beer-deep:#f5cf1c;
    --star:#f5a00b;
    --accent:#f59a14;
    --muted:#555555;
  }
  *{box-sizing:border-box;margin:0;padding:0}
  html,body{width:1200px;height:1074px;overflow:hidden;background:var(--stage)}
  body{position:relative;font-family:'Poppins',sans-serif;color:var(--ink)}
  .screen{position:absolute;width:347px;overflow:hidden}
  .screen-bg{position:absolute;inset:0;background:linear-gradient(180deg,var(--cream) 0%,var(--foam) 18%,var(--beer) 42%,var(--beer-deep) 100%)}
  .screen--splash{left:38px;top:32px;height:568px}
  .screen--splash .screen-bg{background:linear-gradient(180deg,var(--cream) 0%,#f9eab8 22%,var(--beer) 45%,#f7d630 100%)}
  .screen--home{left:423px;top:32px;height:1010px}
  .screen--search{left:808px;top:32px;height:690px}
  .brand{position:absolute;left:0;right:0;text-align:center;font-weight:700;color:var(--ink);letter-spacing:.5px}
  .splash-brand{top:188px;font-size:38px}
  .app-header{position:absolute;left:0;top:0;width:347px;height:90px;background:var(--white);border-radius:0 0 30px 30px}
  .app-header .brand{top:23px;font-size:31px}
  .btn{position:absolute;left:54px;width:241px;height:40px;border-radius:20px;display:flex;align-items:center;justify-content:center;gap:14px;font-size:11px;font-weight:500;letter-spacing:.3px}
  .btn svg{width:11px;height:11px}
  .btn--login{top:282px;background:var(--ink);color:var(--white)}
  .btn--signup{top:335px;background:var(--white);color:var(--ink)}
  .tabs{position:absolute;left:0;width:347px;height:20px}
  .tab{position:absolute;transform:translateX(-50%);font-size:14px;font-weight:600;white-space:nowrap;line-height:20px}
  .tab--a{left:133px}.tab--b{left:243px}
  .tab.is-active{border-bottom:1.5px solid var(--ink)}
  .card{position:absolute;left:15px;width:317px;background:var(--white);border-radius:8px;overflow:hidden}
  .card-photo{width:100%;height:151px}
  .photo-party{background:linear-gradient(135deg,#5a1a10,#c2412a 45%,#e7a04a 70%,#3a1c16)}
  .photo-toast{background:linear-gradient(135deg,#2a221c,#6b4a33 45%,#a98a70 65%,#2d2723)}
  .card-title{display:flex;align-items:center;gap:5px;font-size:14px;font-weight:600;padding:0 14px}
  .stars{display:flex;gap:3px}
  .stars svg{width:12px;height:12px;fill:var(--star)}
  .venue-card .card-title{margin-top:13px}
  .venue-card .meta{font-size:10px;padding:2px 14px 0}
  .heart{position:absolute;right:14px;top:168px;width:12px;height:12px}
  .news-card .card-title{margin-top:13px}
  .news-card .date{font-size:9.5px;font-style:italic;color:var(--muted);padding:3px 14px 0}
  .news-card .body{font-size:9.5px;line-height:17.7px;padding:6px 14px 0}
  .nav{position:absolute;left:15px;width:317px;height:40px;border-radius:20px;background:var(--ink);display:flex;justify-content:space-around;align-items:center;padding:0 6px}
  .nav-item{width:28px;height:28px;border-radius:50%;display:flex;align-items:center;justify-content:center}
  .nav-item svg{width:13px;height:13px;fill:var(--white)}
  .nav-item.is-active{background:var(--accent)}
  .venue-head{position:absolute;left:0;right:0;text-align:center}
  .venue-name{position:absolute;top:108px;left:0;right:0;text-align:center;font-size:25px;font-weight:600}
  .venue-stars{position:absolute;top:141px;left:0;right:0;display:flex;justify-content:center;gap:5px}
  .venue-stars svg{width:12px;height:12px;fill:var(--star)}
  .venue-line{position:absolute;left:0;right:0;text-align:center;font-size:12px}
  .map-area{position:absolute;left:15px;top:229px;width:317px;height:378px;border-radius:8px;background:linear-gradient(120deg,#a7cdc9 0%,#a7cdc9 40%,#f3ecdd 55%,#f6efe2 75%,#a7cdc9 90%)}
</style>
</head>
<body>
<svg width="0" height="0" style="position:absolute">
  <defs>
    <symbol id="i-star" viewBox="0 0 24 24"><path d="M12 2l2.9 6.6 7.1.6-5.4 4.7 1.6 7-6.2-3.7-6.2 3.7 1.6-7L2 9.2l7.1-.6z"/></symbol>
    <symbol id="i-arrow" viewBox="0 0 24 24"><path d="M4 11h12.2l-5-5L13 4.2 21 12l-8 7.8-1.8-1.8 5-5H4z"/></symbol>
    <symbol id="i-heart" viewBox="0 0 24 24"><path d="M12 21s-8-5.2-8-11a4.5 4.5 0 0 1 8-2.8A4.5 4.5 0 0 1 20 10c0 5.8-8 11-8 11z" fill="none" stroke="#262626" stroke-width="2"/></symbol>
    <symbol id="i-home" viewBox="0 0 24 24"><path d="M12 3L1 12h3v9h6v-6h4v6h6v-9h3z"/></symbol>
    <symbol id="i-search" viewBox="0 0 24 24"><path d="M10 3a7 7 0 0 1 5.6 11.2l5.6 5.6-1.8 1.8-5.6-5.6A7 7 0 1 1 10 3zm0 3a4 4 0 1 0 0 8 4 4 0 0 0 0-8z"/></symbol>
    <symbol id="i-list" viewBox="0 0 24 24"><path d="M3 5h3v3H3zm5 0h13v3H8zM3 10.5h3v3H3zm5 0h13v3H8zM3 16h3v3H3zm5 0h13v3H8z"/></symbol>
    <symbol id="i-user" viewBox="0 0 24 24"><path d="M12 2a10 10 0 1 1 0 20 10 10 0 0 1 0-20zm0 4a3.5 3.5 0 1 0 0 7 3.5 3.5 0 0 0 0-7zm0 9c-2.6 0-4.8 1.2-5.8 3a8 8 0 0 0 11.6 0c-1-1.8-3.2-3-5.8-3z"/></symbol>
  </defs>
</svg>

<section class="screen screen--splash">
  <div class="screen-bg" role="img" aria-label="Illustration of beer foam and bubbles with two beer mugs"></div>
  <div class="brand splash-brand">Vexaroo</div>
  <a class="btn btn--login">LOGIN <svg fill="#fff"><use href="#i-arrow"/></svg></a>
  <a class="btn btn--signup">SIGN UP <svg fill="#262626"><use href="#i-arrow"/></svg></a>
</section>

<section class="screen screen--home">
  <div class="screen-bg" role="img" aria-label="Beer foam and bubbles background"></div>
  <header class="app-header"><div class="brand">Vexaroo</div></header>

  <nav class="tabs" style="top:112px"><span class="tab tab--a">Announcments</span><span class="tab tab--b is-active">For You</span></nav>

  <article class="card venue-card" style="top:152px;height:213px">
    <div class="card-photo photo-party" role="img" aria-label="Photo of friends dancing and cheering at a club"></div>
    <div class="card-title">Brassa <span class="stars"><svg><use href="#i-star"/></svg><svg><use href="#i-star"/></svg><svg><use href="#i-star"/></svg><svg><use href="#i-star"/></svg><svg><use href="#i-star"/></svg></span></div>
    <p class="meta">Enterance 100kr, Beer 80kr</p>
    <svg class="heart"><use href="#i-heart"/></svg>
  </article>

  <article class="card venue-card" style="top:385px;height:213px">
    <div class="card-photo photo-toast" role="img" aria-label="Photo of friends toasting beers around a bar table"></div>
    <div class="card-title">Tollbua Bar <span class="stars"><svg><use href="#i-star"/></svg><svg><use href="#i-star"/></svg><svg><use href="#i-star"/></svg><svg><use href="#i-star"/></svg><svg><use href="#i-star"/></svg></span></div>
    <p class="meta">Enterance kr, Beer 76kr</p>
    <svg class="heart"><use href="#i-heart"/></svg>
  </article>

  <nav class="tabs" style="top:620px"><span class="tab tab--a is-active">Announcments</span><span class="tab tab--b">For You</span></nav>

  <article class="card news-card" style="top:658px;height:141px">
    <div class="card-title">Brassa <span class="stars"><svg><use href="#i-star"/></svg><svg><use href="#i-star"/></svg><svg><use href="#i-star"/></svg><svg><use href="#i-star"/></svg><svg><use href="#i-star"/></svg></span></div>
    <p class="date">June 23, 2024</p>
    <p class="body">Brassa extends complimentary admission until 22:00, with a beer price set at 60kr. Please note, the minimum age for entry is 20 years old. Nova Lune will be headlining tonight's entertainment.</p>
  </article>

  <article class="card news-card" style="top:807px;height:141px">
    <div class="card-title">Tollbua Bar <span class="stars"><svg><use href="#i-star"/></svg><svg><use href="#i-star"/></svg><svg><use href="#i-star"/></svg><svg><use href="#i-star"/></svg><svg><use href="#i-star"/></svg></span></div>
    <p class="date">June 23, 2024</p>
    <p class="body">Tollbua Bar is offering complimentary admission until 23:00, with beer priced at 59kr. Kindly be advised that the minimum age for entry is 18 years old. Rex Calder will be headlining tonight's entertainment.</p>
  </article>

  <nav class="nav" style="top:957px">
    <span class="nav-item is-active"><svg><use href="#i-home"/></svg></span>
    <span class="nav-item"><svg><use href="#i-search"/></svg></span>
    <span class="nav-item"><svg><use href="#i-list"/></svg></span>
    <span class="nav-item"><svg><use href="#i-user"/></svg></span>
  </nav>
</section>

<section class="screen screen--search">
  <div class="screen-bg" role="img" aria-label="Beer foam and bubbles background"></div>
  <header class="app-header"><div class="brand">Vexaroo</div></header>
  <h1 class="venue-name">Brassa</h1>
  <div class="venue-stars"><svg><use href="#i-star"/></svg><svg><use href="#i-star"/></svg><svg><use href="#i-star"/></svg><svg><use href="#i-star"/></svg><svg><use href="#i-star"/></svg></div>
  <p class="venue-line" style="top:158px">Opening hours: 20:00- 03:00</p>
  <p class="venue-line" style="top:178px">Age 21+</p>
  <p class="venue-line" style="top:199px;font-weight:600">Beer Cost 80kr</p>
  <div class="map-area" role="img" aria-label="Map of Scandinavia with a pin marking the venue near Oslo"></div>
  <nav class="nav" style="top:620px">
    <span class="nav-item"><svg><use href="#i-home"/></svg></span>
    <span class="nav-item is-active"><svg><use href="#i-search"/></svg></span>
    <span class="nav-item"><svg><use href="#i-list"/></svg></span>
    <span class="nav-item"><svg><use href="#i-user"/></svg></span>
  </nav>
</section>
</body>
</html>
```